Speciality Coffee Shop
Project: Speciality Coffee Shop
Speciality Coffee Shop - Beverages
Creative Brief
Beverages
We chose the name Vireo because it defines the base of coffee and its beginning however our cafe will be serving unique and innovative new drinks which will allow people with different tastes to enjoy the drink. Please update the attached company profile based on the points discussed in the details.
Tornqel58 Tornqel58
Draft #2 : I understand however can you please add a few more slides an input the extra information i provided in the last comment?
Pelomir Pelomir
Hello thanks for rating and comment. First thing we are not professional content writer we are designer. Text content should be provided. You need to hire professional writer for this purpose. I hope you got my point. What I can do is to add the image as you said. Because that is related to design.
Draft #2 : Great job! You are going in the right direction but please find the comments below: 1. The first image you used looks nice but please add other images related to specialty coffee in other slides (such as a Q45 or Slow Brew) 2. Please do not Copy and Paste the text that i gave but use it as a reference. Feel free to change the text to make it more professional. 3. We need a more information on our company profile. Please find below a list of Q&A's for your refference. You can use some of my answers and put them in the profile. Q&A Q: Where is the coffee from? the origin or country imported from A: Colombia, Ethiopia, Kenya, and Panama Q: What is Specialty Coffee? A: According to the Premium Bean Guild of Norland (PBGN), coffee which scores 80 points or above on a 100-point scale is graded "specialty." Specialty coffees are grown in special and ideal climates, and are distinctive because of their full cup taste and little to no defects. In general, we will only select our coffee from suppliers that are certified to be specialty coffee suppliers. Q: Taste A: Each coffee bean tastes different. Some have an after taste of nuts and other have a flowery taste and many more tastes. Weather our customers like their coffee strong (such as an espresso) or sweet (such as our unique Lattes) we will cater to all needs. Q: Short brief on each investor. A: We do not require a brief on each investor individually. The 4 investors Tarek Bensouda, Yousef Qandil, Omar Zaytouni and Hamza Raddaoui have been friends since college. We always had a passion for coffee and were continuously looking for great coffee shops around the country as well as abroad. We finally decided to open our own specialty coffee to ensure that people can trust that it is a specialty coffee shop built by passion rather than financial goals. Q: What are your value propositions or unique selling propositions? A: We will only serve the world's finest specialty coffee, independently tested and scored by certified graders. All our baristas will be certified in the entire aspects of coffee. They will have knowledge from bean to cup to unique latte art. Quality is our number 1 goal. We will never reduce the quality of our items no matter what. Q: What are your vision & mission Our vision is to be the world benchmark for quality coffee. (Please try to think of something better) Our mission is to gather people together over a cup of coffee. (Please try to think of something better.

```html
<!DOCTYPE html>
<html lang="en">
<head>
<meta charset="utf-8">
<title>Vireo Specialty Coffee – Company Profile</title>
<link rel="stylesheet" href="https://fonts.googleapis.com/css2?family=Julius+Sans+One&family=Open+Sans:wght@400;600&family=Great+Vibes&display=swap">
<style>
:root{
  --backdrop:#8b8b8b;
  --ink:#141210;
  --panel:#1d1b19;
  --text:#ece7df;
  --muted:#b8b0a4;
  --line:#d9d2c6;
  --coffee-dark:#2a1c14;
  --coffee-mid:#6b4630;
  --crema:#c8995f;
  --milk:#efe2cc;
}
*{box-sizing:border-box;margin:0;padding:0}
html,body{width:1200px;height:967px;overflow:hidden;background:var(--backdrop)}
body{font-family:"Open Sans",Arial,sans-serif;color:var(--text)}
.profile{position:relative;width:1200px;height:967px;display:grid;grid-template-columns:570px 570px;grid-template-rows:380px 380px;gap:30px 20px;padding:88px 20px}
.spread{position:relative;background:var(--ink);overflow:hidden}
.photo{position:absolute}
.logo{position:absolute;display:flex;flex-direction:column;align-items:center;gap:4px;font-family:"Julius Sans One",Arial,sans-serif;color:var(--text);letter-spacing:8px;font-size:30px;line-height:1}
.logo .dot{width:8px;height:8px;border-radius:50%;background:var(--text)}
.script{font-family:"Great Vibes",cursive;font-weight:400}
.box{position:absolute;border:1px solid var(--line);border-radius:8px;background:rgba(20,18,16,.72);padding:10px 12px}
.box h3{font-family:"Great Vibes",cursive;font-weight:400;font-size:24px;line-height:1;margin-bottom:6px}
.box p,.copy p{font-size:9px;line-height:1.5;color:var(--muted)}
.copy{position:absolute}
.copy h2{font-size:14px;font-weight:600;margin:14px 0 5px}
.copy h2:first-child{margin-top:0}

/* spread 1 */
.s1 .photo{left:0;top:0;width:400px;height:380px;background:radial-gradient(ellipse 120px 80px at 190px 215px,var(--milk) 0 35%,var(--crema) 60%,var(--coffee-mid) 85%,transparent 100%),linear-gradient(160deg,#3a3632,#121110 70%)}
.s1 .logo{left:120px;top:38px}
.s1 .about{left:14px;top:280px;width:180px;height:86px}
.s1 .target{left:206px;top:280px;width:180px;height:86px}
.s1 .box h3{font-family:"Open Sans",Arial,sans-serif;font-size:12px;font-weight:600}
.menu{position:absolute;left:400px;top:0;width:170px;height:380px;background:var(--panel);border-left:1px solid #333;padding:22px 14px;text-align:center}
.menu .title{font-size:28px;line-height:1;white-space:nowrap;margin-bottom:10px}
.menu h4{font-family:"Great Vibes",cursive;font-weight:400;font-size:20px;line-height:1.1;margin:6px 0 4px}
.menu li{list-style:none;font-size:10px;color:var(--muted);line-height:1.6}
.menu .rule{width:60px;height:1px;background:var(--line);margin:8px auto}

/* spread 2 */
.s2 .photo{left:300px;top:0;width:270px;height:380px;background:radial-gradient(circle at 120px 150px,var(--milk) 0 18%,var(--crema) 30%,var(--coffee-mid) 42%,#3a2a20 55%,transparent 70%),radial-gradient(ellipse 40px 70px at 230px 300px,#d9b58a,transparent),linear-gradient(200deg,#4a3a30,#1b1613)}
.s2 .logo{left:22px;top:20px;font-size:24px;letter-spacing:6px}
.s2 .copy{left:22px;top:80px;width:260px}
.investors{position:absolute;left:22px;top:290px;display:flex;gap:14px}
.investors span{display:block;width:92px;height:64px;border:1px solid var(--line);border-radius:6px;background:rgba(20,18,16,.5)}

/* spread 3 */
.s3 .photo{left:0;top:0;width:570px;height:380px;background:radial-gradient(ellipse 70px 110px at 190px 270px,#3d2a1e,transparent 80%),radial-gradient(ellipse 160px 120px at 430px 80px,#4a4440,transparent),linear-gradient(180deg,#2d2a27,#17130f 70%,#3a2a1d)}
.s3 .vision{left:18px;top:18px;width:150px;height:120px}
.s3 .mission{left:400px;top:246px;width:152px;height:118px}
.s3 .logo{left:335px;top:95px}
.s3 .origin{position:absolute;left:325px;top:150px;width:200px;text-align:center;font-size:20px;line-height:1.15;color:var(--text)}

/* spread 4 */
.s4 .photo{left:300px;top:0;width:270px;height:380px;background:radial-gradient(ellipse 60px 110px at 110px 220px,#e4c9a2,#8a5a38 60%,transparent 80%),radial-gradient(ellipse 50px 100px at 200px 200px,#d9b086,transparent 80%),linear-gradient(200deg,#3b332d,#120f0d)}
.s4 .logo{left:420px;top:22px;font-size:24px;letter-spacing:6px}
.s4 .copy{left:22px;top:22px;width:262px}
.s4 .contact{left:430px;top:268px;width:122px;height:96px}
.contact p{display:flex;align-items:center;gap:5px;margin-top:4px}
.contact svg{flex:none}
</style>
</head>
<body>
<main class="profile">

  <section class="spread s1">
    <div class="photo" role="img" aria-label="Latte with milk foam art being poured under an espresso machine"></div>
    <div class="logo">VIREO<span class="dot"></span></div>
    <div class="box about"><h3>About Us</h3><p>A specialty coffee house built by friends with a passion for the perfect cup.</p></div>
    <div class="box target"><h3>Target Market</h3><p>Coffee lovers who value quality, craft and a calm place to meet.</p></div>
    <aside class="menu">
      <div class="title script">Draft Menu*</div>
      <h4>Coffee</h4>
      <ul><li>Espresso</li><li>Cortado</li><li>Flat White</li><li>Cappuccino</li><li>Latte</li><li>Q45 Pour Over</li><li>Slow Brew</li></ul>
      <div class="rule"></div>
      <h4>Sweet</h4>
      <ul><li>Honey Latte</li><li>Mocha</li><li>Cheesecake</li><li>Brownie</li></ul>
    </aside>
  </section>

  <section class="spread s2">
    <div class="photo" role="img" aria-label="Hands holding a cup of latte art beside iced coffees"></div>
    <div class="logo">VIREO<span class="dot"></span></div>
    <div class="copy">
      <h2>Design Concept</h2>
      <p>Dark tones, warm light and clean type reflect the craft behind every cup we serve.</p>
      <h2>Investors</h2>
      <p>Four friends since college share one passion: great specialty coffee built on trust, not profit.</p>
    </div>
    <div class="investors"><span></span><span></span><span></span><span></span></div>
  </section>

  <section class="spread s3">
    <div class="photo" role="img" aria-label="Pour-over coffee dripper on a glass server in a dark cafe"></div>
    <div class="box vision"><h3>Vision</h3><p>Our vision is to be the world benchmark for quality specialty coffee.</p></div>
    <div class="logo">VIREO<span class="dot"></span></div>
    <p class="origin script">Coffee is sourced from Colombia, Ethiopia, Kenya, and Panama</p>
    <div class="box mission"><h3>Mission</h3><p>Our mission is to gather people together over a cup of coffee.</p></div>
  </section>

  <section class="spread s4">
    <div class="photo" role="img" aria-label="Glasses of iced latte with scattered coffee beans"></div>
    <div class="logo">VIREO<span class="dot"></span></div>
    <div class="copy">
      <h2>Specialty Coffee</h2>
      <p>Coffee scoring 80 points or above on a 100-point scale is graded specialty by the PBGN.</p>
      <h2>Taste</h2>
      <p>Nutty, floral or bold, each bean tastes different and we cater to every palate.</p>
      <h2>Unique Selling Propositions</h2>
      <p>Only the world's finest coffee, served by baristas certified from bean to cup.</p>
      <h2>Note</h2>
      <p>Quality is our first goal and we will never reduce it.</p>
    </div>
    <div class="box contact">
      <h3>Contact</h3>
      <p><svg width="9" height="9" viewBox="0 0 10 10"><path d="M2 1l2 2-1 1.5a6 6 0 0 0 2.5 2.5L7 6l2 2-1.5 1.5C4 9 1 6 .5 2.5z" fill="var(--muted)"/></svg>Tel: 555 0142</p>
      <p><svg width="9" height="9" viewBox="0 0 10 10"><rect x=".5" y="2" width="9" height="6" fill="none" stroke="var(--muted)"/><path d="M.5 2l4.5 3.5L9.5 2" fill="none" stroke="var(--muted)"/></svg>hello@vireo.example</p>
    </div>
  </section>

</main>
</body>
</html>
```